IT Company requires new Business Card design.

Over the years we have had a few different business card designs. We are now due for new cards across the board for all staff. We felt this would be a good time to start fresh with a new design. Our traditional card simply had our details on the front, and a list of services on the back. We don't particularly need the list of services, we have had cards where the only thing on the rear of the card was our logo.
Feel free to be creative, we would like our tag line "Complete IT Management" to appear at some point, doesn't necessarily have to be with the logo.
I have attached samples and drafts of various previous cards we have used over the years.
Industry/Entity Type
Business
Look and feel
Each slider illustrates characteristics of the customer's brand and the style your logo design should communicate.

```html
<!DOCTYPE html>
<html lang="en">
<head>
<meta charset="utf-8">
<title>Ridgeway Networking Business Card</title>
<link rel="stylesheet" href="https://fonts.googleapis.com/css2?family=Didact+Gothic&display=swap">
<style>
  :root {
    --card-black: #000000;
    --brand-blue: #3ec4ef;
    --text-white: #ffffff;
    --backdrop: #e9e6e1;
    --shadow: rgba(0, 0, 0, 0.25);
  }
  * { margin: 0; padding: 0; box-sizing: border-box; }
  html, body { width: 1200px; height: 1200px; overflow: hidden; }
  body {
    background: var(--backdrop);
    font-family: "Didact Gothic", "Trebuchet MS", sans-serif;
    position: relative;
  }
  .card { position: absolute; left: 78px; width: 1047px; box-shadow: 0 2px 6px var(--shadow); }
  .card-front { top: 12px; height: 581px; background: var(--card-black); }
  .card-back { top: 615px; height: 585px; background: var(--brand-blue); }

  .contact { position: absolute; left: 47px; top: 118px; color: var(--text-white); }
  .contact-name { font-size: 35px; line-height: 1; }
  .contact-title { font-size: 28px; color: var(--brand-blue); margin-top: 12px; }
  .contact-lines { list-style: none; margin-top: 36px; font-size: 27px; line-height: 36px; }
  .contact-lines .label { display: inline-block; width: 72px; }
  .contact-email { font-size: 27px; margin-top: 36px; }
  .contact-email .domain { color: var(--brand-blue); }

  .services { position: absolute; left: 726px; top: 66px; list-style: none; color: var(--text-white); font-size: 28px; line-height: 36px; }
  .services .num { color: var(--brand-blue); }

  .tagline-band {
    position: absolute; left: 0; right: 0; bottom: 0; height: 44px;
    background: var(--brand-blue); text-align: center; font-size: 28px; line-height: 44px;
  }
  .tagline-band .company { color: var(--card-black); margin-right: 10px; }
  .tagline-band .tagline { color: var(--text-white); }

  .brand-lockup {
    position: absolute; left: 50%; top: 232px; transform: translateX(-50%);
    display: flex; align-items: center; gap: 24px; color: var(--text-white);
  }
  .brand-mark { width: 96px; height: 96px; background: var(--text-white); }
  .brand-name { font-size: 50px; line-height: 1.05; letter-spacing: 2px; }
</style>
</head>
<body>
  <section class="card card-front">
    <div class="contact">
      <h1 class="contact-name">Marcus Reid</h1>
      <p class="contact-title">Operations Manager</p>
      <ul class="contact-lines">
        <li><span class="label">Mob:</span>0412 555 018</li>
        <li><span class="label">Tel:</span>08 5550 1742</li>
        <li><span class="label">Fax:</span>08 5550 1742</li>
      </ul>
      <p class="contact-email">marcus@<span class="domain">ridgewaynetworking.com.au</span></p>
    </div>
    <ol class="services">
      <li><span class="num">01</span>data cabling</li>
      <li><span class="num">02</span>all electrical work</li>
      <li><span class="num">03</span>server racks</li>
      <li><span class="num">04</span>off site back up</li>
      <li><span class="num">05</span>networking</li>
      <li><span class="num">06</span>servers</li>
      <li><span class="num">07</span>workstations</li>
      <li><span class="num">08</span>firewalls</li>
      <li><span class="num">09</span>ADSL connections</li>
      <li><span class="num">10</span>domain names</li>
      <li><span class="num">11</span>PABX systems</li>
    </ol>
    <div class="tagline-band">
      <span class="company">Ridgeway Networking</span><span class="tagline">Complete IT Management</span>
    </div>
  </section>

  <section class="card card-back">
    <div class="brand-lockup">
      <span class="brand-mark"></span>
      <p class="brand-name">RIDGEWAY<br>NETWORKING</p>
    </div>
  </section>
</body>
</html>
```